Harborline Electrical Flyer

An eye catching flyer design which showcases the type of work we do in the electrical industry in Vancouver,BC. The final design should be simple and incorporate our logo. And present a high end company.

Electrical

```html
<!DOCTYPE html>
<html lang="en">
<head>
<meta charset="utf-8">
<title>Harborline Electrical Flyer</title>
<link rel="stylesheet" href="https://fonts.googleapis.com/css2?family=Source+Sans+3:wght@400;600;700&display=swap">
<style>
  :root {
    --yellow: #f6b91a;
    --charcoal: #3d3e40;
    --slate: #5b5c5e;
    --panel-grey: #a7a9ac;
    --white: #ffffff;
    --backdrop: #e6e6e6;
    --sky: #b9d8ec;
  }
  html, body {
    margin: 0;
    width: 990px;
    height: 1200px;
    overflow: hidden;
    background: var(--backdrop);
    font-family: "Source Sans 3", sans-serif;
  }
  .flyer {
    position: absolute;
    left: 87px;
    top: 22px;
    width: 582px;
    height: 826px;
    background: var(--white);
    transform: scale(1.4);
    transform-origin: top left;
    overflow: hidden;
    box-shadow: 0 2px 6px rgba(0,0,0,.25);
  }
  .hero-photo {
    position: absolute;
    left: 0; top: 0;
    width: 582px; height: 324px;
    background: linear-gradient(180deg, #dfeef8 0%, var(--sky) 40%, #eef1f3 70%, #8a8d90 100%);
  }
  .header-shape { position: absolute; left: 0; top: 0; }
  .brand {
    position: absolute;
    left: 36px; top: 32px;
    display: flex; align-items: center; gap: 7px;
    font-weight: 700; font-size: 19px; color: var(--charcoal);
    letter-spacing: .3px;
  }
  .brand-mark { width: 14px; height: 14px; background: var(--yellow); }
  .contact-bar {
    position: absolute; left: 0; top: 324px;
    width: 582px; height: 45px;
    background: var(--slate);
  }
  .phone {
    position: absolute; left: 290px; top: 14px;
    display: flex; align-items: center; gap: 6px;
    color: var(--white); font-weight: 600; font-size: 13.5px;
  }
  .email {
    position: absolute; right: 20px; top: 16px;
    color: var(--white); font-weight: 700; font-size: 11px;
  }
  .about-panel { position: absolute; left: 18px; top: 321px; width: 245px; height: 420px; }
  .panel-shape { position: absolute; left: 0; top: 0; }
  .about-content { position: absolute; left: 13px; top: 30px; width: 220px; color: var(--white); }
  .about-content h2 { margin: 0 0 12px; font-size: 13px; font-weight: 600; }
  .about-content h2.services-heading { margin-bottom: 3px; }
  .about-content p { margin: 0 0 14px; font-size: 11px; line-height: 1.2; text-align: justify; }
  .service-list { list-style: none; margin: 0; padding: 0; }
  .service-list li {
    display: flex; align-items: center; gap: 6px;
    font-size: 15px; line-height: 21.8px;
  }
  .bullet { flex: none; width: 11px; height: 11px; }
  .feature { position: absolute; left: 285px; width: 278px; }
  .feature-tab {
    position: relative; height: 13px; width: 127px;
    font-size: 8px; font-weight: 700; color: var(--white);
    line-height: 13px; padding-left: 5px; box-sizing: border-box;
  }
  .tab-shape { position: absolute; left: 0; top: 0; }
  .feature-tab span { position: relative; }
  .feature-body {
    height: 102px; background: var(--panel-grey);
    display: flex; align-items: center;
  }
  .feature-photo { width: 130px; height: 92px; margin-left: 5px; flex: none; }
  .feature-body p {
    margin: 0 0 0 9px; width: 134px; color: var(--white);
    font-size: 10px; line-height: 1.22; font-weight: 600;
  }
  .footer-rule { position: absolute; left: 0; top: 777px; width: 582px; height: 4px; background: var(--yellow); }
  .footer-rule-grey { position: absolute; left: 0; top: 781px; width: 582px; height: 3px; background: var(--panel-grey); }
  .footer {
    position: absolute; left: 0; top: 784px;
    width: 582px; height: 42px; background: var(--charcoal);
    color: var(--white); font-size: 17px; font-weight: 600;
    text-align: center; line-height: 42px; letter-spacing: .4px;
  }
</style>
</head>
<body>
<main class="flyer">
  <div class="hero-photo" role="img" aria-label="Bright modern living room with white sofa, striped rug, fireplace and pool view"></div>
  <svg class="header-shape" width="582" height="100" viewBox="0 0 582 100">
    <polygon points="0,0 302,0 180,89 0,89" fill="#ffffff"/>
    <polygon points="302,0 312,0 190,89 180,89" fill="#d5e6f2"/>
  </svg>
  <div class="brand"><span class="brand-mark"></span>Harborline Electrical Inc</div>

  <div class="contact-bar">
    <div class="phone">
      <svg width="12" height="12" viewBox="0 0 12 12"><circle cx="6" cy="6" r="5.3" fill="none" stroke="#fff" stroke-width="1"/><path d="M4 3.2l1 1.3-.6.7c.4.9 1 1.5 1.9 1.9l.7-.6 1.3 1-.6 1c-2.2-.2-4.1-2.1-4.3-4.3z" fill="#fff"/></svg>
      604 555 0148
    </div>
    <div class="email">info@harborlineelectrical.ca</div>
  </div>

  <section class="about-panel">
    <svg class="panel-shape" width="245" height="420" viewBox="0 0 245 420">
      <polygon points="0,0 245,0 245,392 122,404 0,392" fill="var(--yellow)"/>
      <polygon points="0,399 122,411 245,399 245,410 122,422 0,410" fill="var(--slate)"/>
    </svg>
    <div class="about-content">
      <h2>About Us</h2>
      <p>We are an electrical contractor serving the lower mainland. Providing the best in customer service and knowledge, to our clients.</p>
      <h2 class="services-heading">Our Services</h2>
      <p>Harborline Electrical offers a wide varierty of services, to meet your electrical needs. Whether it may be residential, commercial or industrial.</p>
      <ul class="service-list">
        <li><svg class="bullet" viewBox="0 0 11 11"><circle cx="5.5" cy="5.5" r="5.5" fill="#fff"/><path d="M4.3 3.2l2.3 2.3-2.3 2.3" fill="none" stroke="#f6b91a" stroke-width="1.4"/></svg>Residental</li>
        <li><svg class="bullet" viewBox="0 0 11 11"><circle cx="5.5" cy="5.5" r="5.5" fill="#fff"/><path d="M4.3 3.2l2.3 2.3-2.3 2.3" fill="none" stroke="#f6b91a" stroke-width="1.4"/></svg>Commercial</li>
        <li><svg class="bullet" viewBox="0 0 11 11"><circle cx="5.5" cy="5.5" r="5.5" fill="#fff"/><path d="M4.3 3.2l2.3 2.3-2.3 2.3" fill="none" stroke="#f6b91a" stroke-width="1.4"/></svg>Lighting</li>
        <li><svg class="bullet" viewBox="0 0 11 11"><circle cx="5.5" cy="5.5" r="5.5" fill="#fff"/><path d="M4.3 3.2l2.3 2.3-2.3 2.3" fill="none" stroke="#f6b91a" stroke-width="1.4"/></svg>Service</li>
        <li><svg class="bullet" viewBox="0 0 11 11"><circle cx="5.5" cy="5.5" r="5.5" fill="#fff"/><path d="M4.3 3.2l2.3 2.3-2.3 2.3" fill="none" stroke="#f6b91a" stroke-width="1.4"/></svg>Fire Alarm</li>
        <li><svg class="bullet" viewBox="0 0 11 11"><circle cx="5.5" cy="5.5" r="5.5" fill="#fff"/><path d="M4.3 3.2l2.3 2.3-2.3 2.3" fill="none" stroke="#f6b91a" stroke-width="1.4"/></svg>Low Voltage Wiring</li>
        <li><svg class="bullet" viewBox="0 0 11 11"><circle cx="5.5" cy="5.5" r="5.5" fill="#fff"/><path d="M4.3 3.2l2.3 2.3-2.3 2.3" fill="none" stroke="#f6b91a" stroke-width="1.4"/></svg>Security</li>
        <li><svg class="bullet" viewBox="0 0 11 11"><circle cx="5.5" cy="5.5" r="5.5" fill="#fff"/><path d="M4.3 3.2l2.3 2.3-2.3 2.3" fill="none" stroke="#f6b91a" stroke-width="1.4"/></svg>Solar Panel</li>
      </ul>
    </div>
  </section>

  <article class="feature" style="top:391px">
    <div class="feature-tab"><svg class="tab-shape" width="127" height="13"><polygon points="0,0 119,0 127,13 0,13" fill="#f6b91a"/></svg><span>LIGHTING EXPERTS</span></div>
    <div class="feature-body">
      <div class="feature-photo" role="img" aria-label="Warmly lit corridor with glowing amber wall panels" style="background:linear-gradient(90deg,#5a2a12,#d9731f 50%,#7a2d10)"></div>
      <p>We provide all your lighting needs to complete any project from small to large.</p>
    </div>
  </article>

  <article class="feature" style="top:518px">
    <div class="feature-tab"><svg class="tab-shape" width="127" height="13"><polygon points="0,0 119,0 127,13 0,13" fill="#f6b91a"/></svg><span>PANELIZED SMART LIGHTING</span></div>
    <div class="feature-body">
      <div class="feature-photo" role="img" aria-label="Smart lighting control panels with wiring and indicator lights" style="background:linear-gradient(90deg,#2b2d33,#4a4f58 55%,#8c8f94)"></div>
      <p>Smart lighting solutions give you endless options with your lights.</p>
    </div>
  </article>

  <article class="feature" style="top:641px">
    <div class="feature-tab"><svg class="tab-shape" width="127" height="13"><polygon points="0,0 119,0 127,13 0,13" fill="#f6b91a"/></svg><span>QUALITY ON TIME...</span></div>
    <div class="feature-body">
      <div class="feature-photo" role="img" aria-label="Electrician holding a yellow hard hat with a tool belt" style="background:linear-gradient(90deg,#b9b4ad,#8a5a48 45%,#d6b236 70%,#6e5c4a)"></div>
      <p>We efficiently manage construction and coordinate with schedules to always give our clients an effortless experience.</p>
    </div>
  </article>

  <div class="footer-rule"></div>
  <div class="footer-rule-grey"></div>
  <footer class="footer">www.harborlineelectrical.ca</footer>
</main>
</body>
</html>
```